Kestrel Building Works Business Card and more!

We need a business card design for Kestrel Building Works Ltd, a respected building company that specialises in high quality designer homes.

We're after a sleek, clean, modern business card that incorporates our new logo (see attached) and colours, with black being the background.

We are Certified Trade Craftsmen and need to include their logo (see attached) on our cards, balancing but not taking over our logo.

Details to be included:

Warren Pike
Director

Phone: 0219462513
Email: kestrelbuild.nz@mailbox-example.nz
Website: www.kestrelbuildingworks.co.nz

Additional Information

A start up website is also under construction and needing attention and letterheads are needed!

We look forward to your designs!

Target Market(s)

30+ people who are interested in building new or renovating current homes

Industry/Entity Type

Construction

Contact Information for Business Card

Warren Pike
Director

Phone: 0219462513
Facebook: www.socialpage-example.com/kestrelbuild.nz

Font styles to use
Serif

Colors

Designer to choose colors to be used in the design.

Requirements
Must have
• Our new logo
• Our colours
• ctc logo

```html
<!DOCTYPE html>
<html lang="en">
<head>
<meta charset="utf-8">
<title>Kestrel Building Works – Business Card</title>
<link rel="stylesheet" href="https://fonts.googleapis.com/css2?family=Roboto+Condensed:wght@700&family=Roboto:wght@400;500&display=swap">
<style>
  :root {
    --backdrop: #2b2b2d;
    --card: #1c1c1d;
    --gold: #c9a16a;
    --white: #f4f4f2;
    --rule: #8a8a8a;
  }
  * { box-sizing: border-box; margin: 0; padding: 0; }
  html, body {
    width: 1200px; height: 900px; overflow: hidden;
    background: var(--backdrop);
  }
  .canvas {
    position: relative; width: 1200px; height: 900px;
  }
  .card {
    position: absolute; left: 250px; width: 700px; height: 390px;
    background: var(--card);
    box-shadow: 0 6px 18px rgba(0,0,0,.45);
  }
  .card--front { top: 45px; }
  .card--back { top: 465px; }

  /* front */
  .brand {
    position: absolute; top: 120px; left: 0; right: 0;
    display: flex; align-items: center; justify-content: center; gap: 14px;
  }
  .brand__mark {
    width: 18px; height: 18px; background: var(--gold);
  }
  .brand__name {
    font-family: "Roboto Condensed", sans-serif; font-weight: 700;
    font-size: 40px; letter-spacing: 3px; color: var(--white);
    text-transform: uppercase;
  }
  .front-web {
    position: absolute; top: 250px; left: 0; right: 0; text-align: center;
    font-family: "Roboto", sans-serif; font-size: 17px; color: var(--white);
    letter-spacing: .3px;
  }
  .cert-badge {
    position: absolute; top: 28px; right: 28px;
    width: 92px; height: 92px; border-radius: 50%;
    background: var(--white);
  }

  /* back */
  .person {
    position: absolute; top: 150px; right: 420px; text-align: right;
  }
  .person__name {
    font-family: "Roboto Condensed", sans-serif; font-weight: 700;
    font-size: 42px; color: var(--gold); letter-spacing: .5px;
    text-transform: uppercase; line-height: 1;
  }
  .person__role {
    margin-top: 8px;
    font-family: "Roboto", sans-serif; font-size: 17px; color: var(--white);
    letter-spacing: 1px; text-transform: uppercase;
  }
  .divider {
    position: absolute; top: 140px; left: 300px; width: 1px; height: 110px;
    background: var(--rule);
  }
  .contacts {
    position: absolute; top: 150px; left: 320px; list-style: none;
    font-family: "Roboto", sans-serif; font-size: 18px; color: var(--white);
  }
  .contacts li {
    display: flex; align-items: center; gap: 10px; height: 24px;
  }
  .contacts svg { width: 15px; height: 15px; flex: none; fill: var(--gold); }
</style>
</head>
<body>
<main class="canvas">
  <section class="card card--front" aria-label="Card front">
    <div class="brand">
      <span class="brand__mark"></span>
      <span class="brand__name">Kestrel Building Works</span>
    </div>
    <p class="front-web">www.kestrelbuildingworks.co.nz</p>
    <div class="cert-badge" role="img" aria-label="Certified Trade Craftsmen badge"></div>
  </section>

  <section class="card card--back" aria-label="Card back">
    <div class="person">
      <h1 class="person__name">Warren Pike</h1>
      <p class="person__role">Director</p>
    </div>
    <div class="divider"></div>
    <ul class="contacts">
      <li>
        <svg viewBox="0 0 16 16" aria-hidden="true"><path d="M3.5 1l2.5 3-1.4 1.8c.9 2 2.6 3.7 4.6 4.6L11 9l3 2.5-1.5 3C7 14.5 1.5 9 1.5 3.5z"/></svg>
        0219462513
      </li>
      <li>
        <svg viewBox="0 0 16 16" aria-hidden="true"><path d="M1 3h14v10H1z M1.8 3.8L8 9l6.2-5.2" fill="none" stroke="#c9a16a" stroke-width="1.4"/></svg>
        kestrelbuild.nz@mailbox-example.nz
      </li>
      <li>
        <svg viewBox="0 0 16 16" aria-hidden="true"><circle cx="8" cy="8" r="6.5" fill="none" stroke="#c9a16a" stroke-width="1.4"/><path d="M1.5 8h13M8 1.5c-3 3.5-3 9.5 0 13M8 1.5c3 3.5 3 9.5 0 13" fill="none" stroke="#c9a16a" stroke-width="1.2"/></svg>
        www.kestrelbuildingworks.co.nz
      </li>
      <li>
        <svg viewBox="0 0 16 16" aria-hidden="true"><rect x="1.5" y="1.5" width="13" height="13"/></svg>
        kestrelbuild.nz
      </li>
    </ul>
  </section>
</main>
</body>
</html>
```